Prepared Meal Company Needs Menu Design

We are a pre-prepared meal delivery company called Grubb Larderly.

We have a menu in excel but needs to be designed to look good and appealing to customers. The menu should be clean, easy to ready, and show:Title (Pupusa)Tags (V, V+, GF - Use a cool vegan logo for the V+ and logo for vegetarian V symbol)Price (12.99)DescriptionBrand colors are orange white and green. Design is clean, crisp and can incorporate natural elements like leaf shaped symbols, etc. Screenshots from our website attached for inspiration.

Target Market(s)

Broad demographics

Industry/Entity Type

Restaurant

Font styles to use
Sans Serif

Requirements
Must have
• The menu design should be commensurate with the website under development
• https://grubblarderly.dishsite.example
Nice to have
• Should have appropriate graphics
Should not have
• Modifiers do not need to be shown (these are shown in the excel only).

```html
<!DOCTYPE html>
<html lang="en">
<head>
<meta charset="utf-8">
<title>Grubb Larderly Breakfast Menu</title>
<link rel="stylesheet" href="https://fonts.googleapis.com/css2?family=Fira+Sans+Condensed:wght@500;600&display=swap">
<style>
  :root {
    --wood-dark: #3f261b;
    --wood-mid: #5a382a;
    --wood-light: #6e4634;
    --rule: rgba(235, 215, 200, 0.55);
    --ink: #ffffff;
    --ink-soft: #f3ece6;
    --brand-orange: #f26a1b;
    --bowl-dark: #2a2624;
    --plate-blue: #a9bcc2;
  }
  * { margin: 0; padding: 0; box-sizing: border-box; }
  html, body { width: 1200px; height: 800px; overflow: hidden; }
  body {
    font-family: "Fira Sans Condensed", "Arial Narrow", sans-serif;
    font-weight: 500;
    color: var(--ink);
    background: linear-gradient(180deg, var(--wood-mid) 0%, var(--wood-dark) 35%, var(--wood-light) 60%, var(--wood-dark) 100%);
    position: relative;
  }
  .brand {
    position: absolute; left: 20px; top: 18px;
    display: flex; align-items: center; gap: 8px;
  }
  .brand-dot {
    width: 34px; height: 34px; border-radius: 50%;
    background: var(--brand-orange); border: 3px solid #fff;
  }
  .brand-name { font-size: 20px; color: #fff; line-height: 1.05; width: 100px; }
  .menu-title {
    position: absolute; left: 200px; top: 26px;
    font-size: 56px; font-weight: 600; line-height: 1; white-space: nowrap;
  }
  .menu-grid {
    position: absolute; left: 0; top: 119px; width: 1200px; height: 644px;
    display: grid; grid-template-columns: 600px 600px; grid-template-rows: repeat(4, 161px);
    border-top: 1px solid var(--rule);
  }
  .dish { position: relative; border-bottom: 1px solid var(--rule); }
  .dish:nth-child(odd) { border-right: 1px solid var(--rule); }
  .dish-text {
    position: absolute; left: 18px; top: 0; width: 215px; height: 100%;
    display: flex; flex-direction: column; justify-content: center; gap: 14px;
  }
  .dish-name { font-size: 22px; font-weight: 500; line-height: 1.35; }
  .dish-desc { font-size: 13px; line-height: 1.35; color: var(--ink-soft); }
  .dish-text.tight { gap: 3px; }
  .dish-text.tight .dish-name { line-height: 1.25; }
  .dish-text.tight .dish-desc { font-size: 11.5px; line-height: 1.3; }
  .dish-price {
    position: absolute; left: 238px; top: 24px;
    font-size: 36px; font-weight: 600; line-height: 1;
  }
  .dish-photo { position: absolute; left: 354px; top: 14px; width: 238px; height: 133px; }
  .photo-bowl { background: radial-gradient(ellipse at center, #c9a27a 0%, #8a5a3a 30%, var(--bowl-dark) 48%, #e9e4df 70%, #d6d0ca 100%); }
  .photo-red { background: radial-gradient(ellipse at center, #b5421f 0%, #7a2a14 32%, var(--bowl-dark) 48%, #ebe6e0 70%, #d8d2cc 100%); }
  .photo-green { background: radial-gradient(ellipse at center, #c4622c 0%, #5a6a2a 30%, var(--bowl-dark) 50%, #e3dfda 72%, #cfc9c3 100%); }
  .photo-plate { background: radial-gradient(ellipse at center, #d9b890 0%, #7d8f86 30%, var(--plate-blue) 55%, #e8e4df 80%, #d5cfc8 100%); }
  .photo-acai { background: radial-gradient(ellipse at center, #d8a0a0 0%, #b9c4c4 45%, #8fa3a8 60%, #e8e4df 80%, #d5cfc8 100%); }
  .photo-yogurt { background: radial-gradient(ellipse at center, #c59a6c 0%, #f3efe9 30%, var(--bowl-dark) 52%, #e9e4df 72%, #d6d0ca 100%); }
  .site-url {
    position: absolute; left: 0; width: 1200px; top: 770px;
    text-align: center; font-size: 16px;
  }
</style>
</head>
<body>
  <div class="brand">
    <span class="brand-dot"></span>
    <span class="brand-name">Grubb Larderly</span>
  </div>
  <h1 class="menu-title">Breakfast - ALL MENU ITEMS SOY FREE</h1>

  <main class="menu-grid">
    <section class="dish">
      <div class="dish-text">
        <h2 class="dish-name">Cinnamon-Apple<br>Sunrise Oats (V+, GF)</h2>
        <p class="dish-desc">Almond Milk &amp; Ceylon Cinnamon, Marinated Golden Raisins, Macca Powder, Apple-Pecan Crumble</p>
      </div>
      <p class="dish-price">6.99 $</p>
      <div class="dish-photo photo-bowl" role="img" aria-label="Bowl of cinnamon apple oats topped with pecan crumble"></div>
    </section>

    <section class="dish">
      <div class="dish-text tight">
        <h2 class="dish-name">Pomegranate &amp;<br>Saffron Shakshuka<br>(V, GF, Dairy Free)</h2>
        <p class="dish-desc">2 Soft Yolk Eggs over Roasted Tomatoes, Onions &amp; Peppers, Garden Herb Oil, Rosemary, Oregano &amp; Thyme with Handmade Gluten-Free Flatbread</p>
      </div>
      <p class="dish-price">10.99 $</p>
      <div class="dish-photo photo-red" role="img" aria-label="Pan of shakshuka with eggs and gluten-free flatbread"></div>
    </section>

    <section class="dish">
      <div class="dish-text">
        <h2 class="dish-name">Acai Yogurt (V, GF)</h2>
        <p class="dish-desc">Coconut, Goji, Seasonal Fruit, Crunchy Chia Seeds, Ceylon Cinnamon</p>
      </div>
      <p class="dish-price">7.99 $</p>
      <div class="dish-photo photo-acai" role="img" aria-label="Acai yogurt bowl with goji, strawberries, blueberries and chia"></div>
    </section>

    <section class="dish">
      <div class="dish-text">
        <h2 class="dish-name">Sweet Potato<br>Hash (V+, GF)</h2>
        <p class="dish-desc">Broccolini, Cherry Tomato, Asparagus, Roasted Peppers &amp; Onions, Rosemary-Nutritional Yeast</p>
      </div>
      <p class="dish-price">8.99 $</p>
      <div class="dish-photo photo-green" role="img" aria-label="Bowl of sweet potato hash with broccolini and asparagus"></div>
    </section>

    <section class="dish">
      <div class="dish-text">
        <h2 class="dish-name">Seedline 7<br>Cereal &amp; Yogurt (V)</h2>
        <p class="dish-desc">Apricot-Pear Compote, Almond &amp; Saba Drizzle</p>
      </div>
      <p class="dish-price">7.49 $</p>
      <div class="dish-photo photo-yogurt" role="img" aria-label="Bowl of yogurt topped with sprouted grain cereal and an edible flower"></div>
    </section>

    <section class="dish">
      <div class="dish-text">
        <h2 class="dish-name">Mom's Frittata<br>(V, GF)</h2>
        <p class="dish-desc">Roasted Cherry Tomato, Goat Cheese &amp; Baby Spinach with Sweet Potato Homefries</p>
      </div>
      <p class="dish-price">11.99 $</p>
      <div class="dish-photo photo-green" role="img" aria-label="Bowl of frittata with cherry tomatoes and spinach"></div>
    </section>

    <section class="dish">
      <div class="dish-text">
        <h2 class="dish-name">St. Benedict's Eggs<br>(V, Dairy Free)</h2>
        <p class="dish-desc">2 Soft Yolk Eggs over Rosemary Polenta, Caramelized Onion, Mushrooms &amp; Asparagus, Lemon</p>
      </div>
      <p class="dish-price">9.49 $</p>
      <div class="dish-photo photo-plate" role="img" aria-label="Plate of poached eggs over polenta with mushrooms and asparagus"></div>
    </section>

    <section class="dish">
      <div class="dish-text">
        <h2 class="dish-name">Country Style<br>Breakfast Sandwich (V)</h2>
        <p class="dish-desc">Arugula, Goat Cheese, Cherry Tomatoes &amp; Lemon with Mom's Fritatta on Seedline 7 Bread</p>
      </div>
      <p class="dish-price">13.99 $</p>
      <div class="dish-photo photo-plate" role="img" aria-label="Open breakfast sandwich with frittata, arugula and goat cheese on a plate"></div>
    </section>
  </main>

  <p class="site-url">https://grubblarderly.dishsite.example/</p>
</body>
</html>
```